QR TILL WORKS , CREDIT CARD PROCESSING EQUIPMENT

qrtillworks is a sub division of Tallow a credit car processing co.
harold finch
14 cedar hollow ln
brookmere pa 07312
suite 412

qrtillworks.example
cell 555-214-7730
office 555-861-2093
we sell pos systems to merchant who want to accept credit cards at there retail location.
black card would be nice buit open to different ideas

Target Market(s)

retail merchants

Industry/Entity Type

credit card processing

Contact Information for Business Card

card should include web site phone address

Colors

Designer to choose colors to be used in the design.

Requirements
Should not have
• red

```html
<!DOCTYPE html>
<html lang="en">
<head>
<meta charset="UTF-8">
<title>QR Till Works – Business Card</title>
<link href="https://fonts.googleapis.com/css2?family=Montserrat:wght@400;500;700&display=swap" rel="stylesheet">
<style>
  :root {
    --backdrop: #d9d6d2;
    --card: #1c1c1c;
    --accent: #f2c418;
    --text: #f2f2f2;
    --muted: #cfcfcf;
  }
  * { box-sizing: border-box; margin: 0; padding: 0; }
  html, body { width: 1200px; height: 716px; overflow: hidden; }
  body {
    background: var(--backdrop);
    font-family: "Montserrat", sans-serif;
    position: relative;
  }
  .card {
    position: absolute;
    top: 204px;
    width: 540px;
    height: 308px;
    background: var(--card);
    border-radius: 4px;
    box-shadow: 0 14px 30px rgba(0,0,0,.28);
  }
  .card--front { left: 40px; border-bottom: 6px solid var(--accent); }
  .card--back { left: 620px; border: 2px solid var(--accent); }

  .wordmark {
    position: absolute;
    font-weight: 700;
    color: var(--text);
    letter-spacing: .02em;
    white-space: nowrap;
  }
  .card--front .wordmark {
    left: 50%; top: 50%;
    transform: translate(-50%, -50%);
    font-size: 46px;
    color: var(--muted);
  }
  .card--back .wordmark {
    left: 34px; top: 96px;
    font-size: 32px;
    line-height: 1.15;
  }
  .divider {
    position: absolute;
    left: 250px; top: 66px;
    width: 2px; height: 176px;
    background: var(--accent);
  }
  .contact {
    position: absolute;
    left: 270px; top: 70px;
    width: 250px;
    color: var(--text);
    font-size: 12.5px;
    line-height: 1.45;
  }
  .contact__name {
    color: var(--accent);
    font-weight: 700;
    font-size: 20px;
    letter-spacing: .03em;
    line-height: 1.1;
  }
  .contact__title {
    font-size: 12.5px;
    letter-spacing: .08em;
    margin-bottom: 8px;
  }
  .contact__row { display: flex; align-items: center; gap: 6px; }
  .contact__row svg { width: 11px; height: 11px; flex: none; }
  .contact__address { margin-bottom: 2px; }
</style>
</head>
<body>
  <section class="card card--front">
    <span class="wordmark">QR TILL WORKS</span>
  </section>

  <section class="card card--back">
    <span class="wordmark">QR TILL<br>WORKS</span>
    <span class="divider"></span>
    <div class="contact">
      <p class="contact__name">DANA WHITLOCK</p>
      <p class="contact__title">DIRECTOR</p>
      <p class="contact__address">14 cedar hollow ln<br>brookmere pa 07312 suite 412</p>
      <p class="contact__row">
        <svg viewBox="0 0 12 12"><path d="M3 1l2 2.5-1.2 1.3a7 7 0 0 0 3.4 3.4L8.5 7 11 9l-1.2 2C5 11 1 7 1 2.2z" fill="var(--accent)"/></svg>
        555-861-2093
      </p>
      <p class="contact__row">
        <svg viewBox="0 0 12 12"><rect x="3" y="1" width="6" height="10" rx="1" fill="none" stroke="var(--accent)" stroke-width="1.3"/><circle cx="6" cy="9" r=".7" fill="var(--accent)"/></svg>
        555-214-7730
      </p>
      <p class="contact__row">
        <svg viewBox="0 0 12 12"><rect x="1" y="2.5" width="10" height="7" fill="none" stroke="var(--accent)" stroke-width="1.2"/><path d="M1 2.5l5 4 5-4" fill="none" stroke="var(--accent)" stroke-width="1.2"/></svg>
        info@qrtillworks.example
      </p>
      <p class="contact__row">
        <svg viewBox="0 0 12 12"><circle cx="6" cy="6" r="5" fill="none" stroke="var(--accent)" stroke-width="1.2"/><path d="M1 6h10M6 1c-2.5 3-2.5 7 0 10M6 1c2.5 3 2.5 7 0 10" fill="none" stroke="var(--accent)" stroke-width="1"/></svg>
        www.qrtillworks.example
      </p>
    </div>
  </section>
</body>
</html>
```